Quellor Health — Premium Telehealth Marketing Website

Quellor Health is a modern, cash-pay telehealth brand offering prescription weight-loss (GLP-1) and sexual-health treatment online, with licensed US providers — no insurance required. We're building a premium, trustworthy direct-to-consumer healthcare brand in the same tier as Tavrin, Ux, and Plimso.

We need a clean, modern, premium marketing website design — warm and trustworthy, not cold or clinical. Think high-end wellness brand: generous whitespace, elegant typography, calm and confident. It should feel medically credible but human and approachable.

WHAT WE NEED DESIGNED (3 core templates that define the whole site):

1. Homepage — the brand showcase that establishes the full visual language (hero, sections, product highlights, how-it-works, trust elements, footer).

2. Product / Treatment page template — a reusable layout for any medication (transparent pricing, how it works, what's included, clinical info, safety, clear call-to-action). We'll reuse this pattern for all treatments.

3. Interior / Content page template — a flexible layout for sub-pages like How It Works, About, Contact, FAQ, and legal pages.

We'll implement the final site ourselves in React/Next.js + Tailwind CSS, so clean, well-structured design (and HTML/CSS if you provide it) is a strong plus.

BRAND DIRECTION (already established — please design within this):

- Logo: lowercase wordmark "quellor." with the period in gold (see attached). Please build the design around this existing logo.
- Colors: deep navy (#0B1B33 and #14315C) with a warm gold accent (#E0A458); soft light backgrounds (#EEF3F9, #FBFCFE).
- Typography: a refined serif for headlines (e.g., Fraunces) paired with a clean sans-serif for body (e.g., Inter).
- Tone: premium, warm, trustworthy, human.

INSPIRATION / QUALITY BAR: Tavrin (tavrin.example), Ux (ux.example), Plimso — the polished DTC healthcare aesthetic. We want that tier of quality, with our own warmer navy-and-gold identity.

Industry/Entity Type

Telemedicine

Coding

Coded - Design and coding required

Number of Pages Required

3 page

Requirements
Nice to have
• Side Scrolling Medictions bar like on Ux.example

```html
<!DOCTYPE html>
<html lang="en">
<head>
<meta charset="utf-8">
<title>Semaglutide Weekly Injections — Quellor Health</title>
<link href="https://fonts.googleapis.com/css2?family=Fraunces:opsz,wght@9..144,300;9..144,400;9..144,500&family=Inter:wght@400;500;600&display=swap" rel="stylesheet">
<style>
:root{
  --navy:#0B1B33;
  --navy-2:#14315C;
  --gold:#E0A458;
  --cream:#FBFAF6;
  --band:#F5F3EE;
  --line:#E8E4DC;
  --text:#3E4A5C;
  --muted:#6B7586;
  --card:#FFFFFF;
}
*{box-sizing:border-box;margin:0;padding:0}
html,body{width:1200px;height:3688px;overflow:hidden}
body{background:var(--cream);font-family:'Inter',sans-serif;color:var(--navy);position:relative}
.serif{font-family:'Fraunces',serif}
a{color:inherit;text-decoration:none}

/* header */
.site-header{height:66px;border-bottom:1px solid var(--line);display:flex;align-items:center;padding:0 87px;position:relative}
.wordmark{font-family:'Inter',sans-serif;font-weight:600;font-size:19px;color:var(--navy);background:#EEF3F9;padding:5px 9px;border-radius:4px}
.main-nav{position:absolute;left:337px;display:flex;gap:34px;font-size:12.5px;font-weight:500;height:66px;align-items:center}
.main-nav a{padding:6px 0}
.main-nav .active{border-bottom:2px solid var(--navy)}
.header-actions{margin-left:auto;display:flex;gap:14px}
.btn-pill{height:47px;border-radius:24px;display:flex;align-items:center;justify-content:center;font-size:12.5px;font-weight:600;letter-spacing:.08em}
.btn-outline{width:122px;border:1.5px solid var(--navy)}
.btn-gold{width:149px;background:var(--gold);color:var(--navy)}

/* hero */
.hero{height:650px;position:relative}
.product-frame{position:absolute;left:112px;top:135px;width:381px;height:366px;border-radius:22px;background:#F1EBE2;box-shadow:0 14px 40px rgba(11,27,51,.10)}
.product-photo{position:absolute;left:41px;top:32px;width:298px;height:298px;background:linear-gradient(90deg,#EEE6DA 0%,#E4D8C8 65%,#14233B 85%,#0E1B30 100%)}
.seal{position:absolute;right:20px;bottom:22px;width:60px;height:60px;border-radius:50%;background:#F7F4EF;border:2px solid #fff;box-shadow:0 2px 6px rgba(0,0,0,.12)}
.thumbs{position:absolute;left:180px;top:515px;display:flex;gap:12px}
.thumb{width:52px;height:52px;border-radius:8px;background:#E9E0D3}
.thumb.active{border:2px solid var(--navy)}
.thumb.t2{background:linear-gradient(135deg,#C9B9A2,#2A3650)}
.thumb.t3{background:linear-gradient(135deg,#F2EAE0,#D9BFA8)}
.thumb.t4{background:linear-gradient(135deg,#E4D8C4,#CDB58E)}

.hero-copy{position:absolute;left:585px;top:70px;width:528px}
.eyebrow-row{display:flex;align-items:baseline;gap:14px}
.eyebrow{font-size:10.5px;font-weight:600;letter-spacing:.16em;color:var(--gold);text-transform:uppercase}
.licensed{font-size:11.5px;color:var(--navy-2);font-weight:500}
.hero-title{font-family:'Fraunces',serif;font-weight:300;font-size:44px;line-height:1.18;margin-top:24px}
.hero-points{list-style:none;margin-top:26px;font-size:13.5px;line-height:1}
.hero-points li{margin-bottom:20px}
.btn-primary{display:flex;height:51px;border-radius:26px;background:var(--navy);color:#fff;align-items:center;justify-content:center;font-size:14px;font-weight:600;margin-top:14px}
.safety-link{display:block;text-align:center;font-size:9.5px;color:var(--muted);text-decoration:underline;margin-top:14px}
.hero-accordion{margin-top:20px;border-top:1px solid var(--line)}
.acc-row{height:51px;border-bottom:1px solid var(--line);display:flex;align-items:center;justify-content:space-between;font-size:13.5px;font-weight:600}

/* section headings */
.section-label{font-size:10.5px;font-weight:600;letter-spacing:.16em;color:var(--gold);text-transform:uppercase;text-align:center}
.section-title{font-family:'Fraunces',serif;font-weight:400;font-size:42px;line-height:1.2;text-align:center;margin-top:18px}
.section-sub{font-size:13.5px;color:var(--muted);text-align:center;margin-top:22px}

/* included */
.included{height:797px;padding-top:175px}
.included-grid{display:flex;gap:27px;padding:0 87px;margin-top:60px}
.feature-card{width:236px;height:279px;background:var(--card);border:1px solid var(--line);border-radius:14px;padding:33px 33px}
.feature-icon{width:36px;height:36px;border-radius:8px;background:#FBEEDC;display:flex;align-items:center;justify-content:center}
.feature-card h3{font-family:'Fraunces',serif;font-weight:500;font-size:17px;line-height:1.2;margin-top:22px}
.feature-card p{font-size:12.5px;line-height:1.62;color:var(--text);margin-top:12px}

/* journey */
.journey{height:637px;background:var(--band);padding-top:108px}
.steps{position:relative;margin:50px 0 0 244px;width:700px}
.steps::before{content:"";position:absolute;left:8px;top:10px;height:278px;width:2px;background:var(--gold)}
.step{position:relative;padding-left:36px;margin-bottom:38px}
.step::before{content:"";position:absolute;left:0;top:2px;width:18px;height:18px;border-radius:50%;background:var(--navy);box-shadow:0 0 0 3px var(--gold) inset,0 0 0 0 #fff;border:3px solid var(--gold)}
.step h4{font-size:15px;font-weight:600}
.step p{font-size:12.5px;line-height:1.7;color:var(--text);margin-top:8px}

/* faq */
.faq{height:1072px;padding-top:112px}
.faq-list{width:708px;margin:70px auto 0}
.faq-item{background:var(--card);border:1px solid var(--line);border-radius:12px;margin-bottom:19px;box-shadow:0 4px 14px rgba(11,27,51,.04)}
.faq-head{height:65px;padding:0 26px;display:flex;align-items:center;justify-content:space-between;font-size:15px;font-weight:500}
.faq-body{padding:0 26px 40px;font-size:12.8px;line-height:1.72;color:var(--text)}
.faq-body strong{color:var(--navy);font-weight:600}
.faq-body ul{margin:16px 0 10px 20px}
.faq-body li{margin-bottom:8px}
.faq-open .faq-head{height:65px}

/* footer */
.site-footer{position:absolute;left:0;top:3156px;width:1200px;height:532px;background:var(--navy);color:#C9D3E2;padding:0 87px}
.footer-top{display:flex;padding-top:82px;height:318px}
.footer-brand{width:354px}
.footer-logo{display:inline-block;background:#fff;color:var(--navy);font-weight:600;font-size:15px;padding:2px 7px}
.footer-brand p{font-size:12.5px;line-height:1.7;color:#8FA6C7;margin-top:42px;width:270px}
.footer-col{width:240px}
.footer-col h5{font-size:11px;letter-spacing:.16em;font-weight:600;color:#fff}
.footer-col ul{list-style:none;margin-top:30px}
.footer-col li{font-size:12.5px;color:#fff;margin-bottom:21px}
.footer-col li.dim{color:#8FA6C7}
.footer-rule{border-top:1px solid #243656}
.disclaimer{font-size:10.5px;line-height:1.8;color:#8FA6C7;margin-top:22px}
.copyright{font-size:10.5px;color:#8FA6C7;margin-top:16px}
.legal{display:flex;gap:26px;margin-top:26px;font-size:10.5px;color:#8FA6C7}
.legal a{text-decoration:underline}
</style>
</head>
<body>

<header class="site-header">
  <a class="wordmark" href="#">quellor.</a>
  <nav class="main-nav">
    <a class="active" href="#">Products</a><a href="#">How It Works</a><a href="#">FAQ</a><a href="#">About Us</a>
  </nav>
  <div class="header-actions">
    <a class="btn-pill btn-outline" href="#">SUPPORT</a>
    <a class="btn-pill btn-gold" href="#">GET STARTED</a>
  </div>
</header>

<section class="hero">
  <div class="product-frame">
    <div class="product-photo" role="img" aria-label="Hand holding a semaglutide injection pen beside a vase with greenery"></div>
    <div class="seal" role="img" aria-label="Certification seal"></div>
  </div>
  <div class="thumbs">
    <div class="thumb active" role="img" aria-label="Injection pen thumbnail"></div>
    <div class="thumb t2" role="img" aria-label="Packaging thumbnail"></div>
    <div class="thumb t3" role="img" aria-label="Hand thumbnail"></div>
    <div class="thumb t4" role="img" aria-label="Supply detail thumbnail"></div>
  </div>

  <div class="hero-copy">
    <div class="eyebrow-row"><span class="eyebrow">FDA &amp; HSA/FSA Eligible</span><span class="licensed">✓ Licensed U.S. Providers</span></div>
    <h1 class="hero-title">Semaglutide Weekly<br>Injections</h1>
    <ul class="hero-points">
      <li>● Semaglutide is an FDA-approved weekly injection for weight care</li>
      <li>● Clinically proven to help achieve up to 15% weight loss, on average</li>
    </ul>
    <a class="btn-primary" href="#">Get started</a>
    <a class="safety-link" href="#">Important safety information</a>
    <div class="hero-accordion">
      <div class="acc-row">Meet Semaglutide Care <svg width="12" height="8" viewBox="0 0 12 8"><path d="M1 1l5 5 5-5" fill="none" stroke="#0B1B33" stroke-width="1.5"/></svg></div>
      <div class="acc-row">About the ingredients <svg width="12" height="8" viewBox="0 0 12 8"><path d="M1 1l5 5 5-5" fill="none" stroke="#0B1B33" stroke-width="1.5"/></svg></div>
      <div class="acc-row">How to take <svg width="12" height="8" viewBox="0 0 12 8"><path d="M1 1l5 5 5-5" fill="none" stroke="#0B1B33" stroke-width="1.5"/></svg></div>
    </div>
  </div>
</section>

<section class="included">
  <p class="section-label">A Complete Care Program</p>
  <h2 class="section-title">Everything you need, in one<br>transparent price.</h2>
  <p class="section-sub">No hidden doctor fees, co-pays, or surprise pharmacy costs.</p>
  <div class="included-grid">
    <article class="feature-card">
      <div class="feature-icon"><svg width="16" height="16" viewBox="0 0 16 16" fill="none" stroke="#E0A458" stroke-width="1.3"><rect x="2" y="3" width="12" height="3"/><path d="M3 6v7h10V6M6 9h4"/></svg></div>
      <h3>Prescribed<br>Medication</h3>
      <p>Genuine Semaglutide compound tailored to your specific dosage, prepared in a state-licensed compounding pharmacy.</p>
    </article>
    <article class="feature-card">
      <div class="feature-icon"><svg width="16" height="16" viewBox="0 0 16 16" fill="none" stroke="#E0A458" stroke-width="1.3"><circle cx="6" cy="5" r="2.5"/><path d="M1.5 13c.5-3 2.3-4.5 4.5-4.5s4 1.5 4.5 4.5M12 5v4M10 7h4"/></svg></div>
      <h3>Doctor Consultation</h3>
      <p>Complete medical evaluation and continuous chat access to U.S.-licensed clinicians to review dosing adjustments.</p>
    </article>
    <article class="feature-card">
      <div class="feature-icon"><svg width="16" height="16" viewBox="0 0 16 16" fill="none" stroke="#E0A458" stroke-width="1.3"><path d="M3 13l3-3M5 11l6-6 1.5 1.5-6 6zM11 5l2-2M12 2l2 2"/></svg></div>
      <h3>All Injection Supplies</h3>
      <p>Sterile single-use syringes and alcohol prep pads shipped automatically with each monthly package.</p>
    </article>
    <article class="feature-card">
      <div class="feature-icon"><svg width="16" height="16" viewBox="0 0 16 16" fill="none" stroke="#E0A458" stroke-width="1.3"><path d="M8 2v12M2 8h12M4 4l8 8M12 4l-8 8"/><circle cx="8" cy="8" r="2"/></svg></div>
      <h3>Cold-Chain Delivery</h3>
      <p>Refrigerated shipping in insulated containers to preserve medication potency and active molecule integrity.</p>
    </article>
  </div>
</section>

<section class="journey">
  <p class="section-label">Your Clinical Journey</p>
  <h2 class="section-title">How your care is established</h2>
  <div class="steps">
    <div class="step"><h4>1. Online Medical Evaluation</h4><p>You complete a 15-minute diagnostic quiz covering health history, previous weight-loss efforts, and medication contraindications.</p></div>
    <div class="step"><h4>2. Provider Treatment Formulation</h4><p>A physician reviews your chart to verify suitability. If approved, they formulate your initial prescription and calculate starting dosages.</p></div>
    <div class="step"><h4>3. Direct Prescription Shipping</h4><p>Our state-certified partner pharmacy compounds the order, packs it in thermal-insulated containers, and ships it via express delivery.</p></div>
  </div>
</section>

<section class="faq">
  <p class="section-label">Clinical Information &amp; Guidelines</p>
  <h2 class="section-title">Clinical Information &amp; FAQs</h2>
  <p class="section-sub">Important details regarding side effects, dosing protocols, and prescribing criteria.</p>
  <div class="faq-list">
    <div class="faq-item faq-open">
      <div class="faq-head">Important Safety Information &amp; Side Effects <svg width="12" height="8" viewBox="0 0 12 8"><path d="M1 7l5-5 5 5" fill="none" stroke="#0B1B33" stroke-width="1.5"/></svg></div>
      <div class="faq-body">
        <p>Prescription weight-loss medications are clinically sound but carry potential risks. It is important to review all medical advisories before starting therapy.</p>
        <p style="margin-top:22px"><strong>Common Side Effects include:</strong></p>
        <ul>
          <li>Mild to moderate nausea or abdominal discomfort</li>
          <li>Occasional indigestion, acid reflux, or bloating</li>
          <li>Mild constipation or diarrhea during initial dose escalations</li>
          <li>Temporary fatigue during the first week of treatment</li>
        </ul>
        <p><strong>Critical Warnings:</strong> Semaglutide should not be used by patients with a personal or family history of Medullary Thyroid Carcinoma (MTC) or Multiple Endocrine Menoplasia syndrome type 2 (MEN 2). Discuss all existing medical conditions, thyroid issues, or pancreatitis history during your intake evaluation.</p>
      </div>
    </div>
    <div class="faq-item"><div class="faq-head">Active Ingredients &amp; Efficacy Details <svg width="12" height="8" viewBox="0 0 12 8"><path d="M1 1l5 5 5-5" fill="none" stroke="#0B1B33" stroke-width="1.5"/></svg></div></div>
    <div class="faq-item"><div class="faq-head">How to Self-Administer &amp; Dosing Schedule <svg width="12" height="8" viewBox="0 0 12 8"><path d="M1 1l5 5 5-5" fill="none" stroke="#0B1B33" stroke-width="1.5"/></svg></div></div>
    <div class="faq-item"><div class="faq-head">Refills, Shipping, &amp; Cancellation Policies <svg width="12" height="8" viewBox="0 0 12 8"><path d="M1 1l5 5 5-5" fill="none" stroke="#0B1B33" stroke-width="1.5"/></svg></div></div>
  </div>
</section>

<footer class="site-footer">
  <div class="footer-top">
    <div class="footer-brand">
      <span class="footer-logo">quellor.</span>
      <p>Premium online telehealth providing doctor-prescribed treatments without the hassle of traditional clinics.</p>
    </div>
    <div class="footer-col"><h5>TREATMENTS</h5><ul><li>Weight Loss (GLP-1)</li><li>Sexual Health Care</li><li>Semaglutide Injections</li><li>Sildenafil (ED Treatment)</li></ul></div>
    <div class="footer-col"><h5>COMPANY</h5><ul><li>About Us</li><li>How It Works</li><li>Contact Support</li><li>Frequently Asked Questions</li></ul></div>
    <div class="footer-col"><h5>CONTACT</h5><ul><li>support@quellorhealth.example</li><li>1 (800) 555-0142</li><li class="dim">Mon–Fri: 9am – 6pm EST</li></ul></div>
  </div>
  <div class="footer-rule"></div>
  <p class="disclaimer">Disclaimer: Quellor Health does not provide medical services directly. All medical consultations and treatment decisions are performed by independent, US-licensed physicians operating through our secure telehealth platform. Prescription availability is subject to medical provider approval. GLP-1 medications can have serious side effects; please read all safety and prescribing information before initiating care.</p>
  <p class="copyright">© 2026 Quellor Health Inc. All rights reserved.</p>
  <div class="legal"><a href="#">Privacy Policy</a><a href="#">Terms of Service</a><a href="#">Telehealth Consent</a></div>
</footer>

</body>
</html>
```